Bref créative
Business Cards & stationery for Drywall Contractor
Business card, invoice, fax, letterhead, envelopes
Professional
Radoslav Benek
Owner
N/A - We do not want our address on the business card
info@tmkbuildingworks.example
www.tmkbuildingworks.example
SCC284730592
"Certified Specialty Contractor"
Framing; Drywall Installation & Finishing; Wall Textures; Acoustical Ceilings; Raised Access Floors; Commercial & Residential; New Construction;
Remodeling

```html
<!DOCTYPE html>
<html lang="en">
<head>
<meta charset="utf-8">
<title>TMK Building Works – Stationery Set</title>
<link href="https://fonts.googleapis.com/css2?family=Montserrat:wght@600;800&family=Open+Sans:wght@400;600&display=swap" rel="stylesheet">
<style>
:root{
  --bg:#e6e1d9;
  --red:#c3161c;
  --red-dark:#8e0e12;
  --ink:#1d1d1d;
  --grey:#8a8a8a;
  --line:#cfcfcf;
  --paper:#ffffff;
  --faint:#f3e3e3;
}
*{box-sizing:border-box;margin:0;padding:0}
html,body{width:1200px;height:362px;overflow:hidden;background:var(--bg)}
body{position:relative;font-family:"Open Sans",Arial,sans-serif;color:var(--ink)}
.piece{position:absolute;background:var(--paper);box-shadow:0 1px 3px rgba(0,0,0,.25)}
.brand{font-family:"Montserrat",Arial,sans-serif;font-weight:800;color:var(--red);display:flex;align-items:center;gap:4px;line-height:1}
.brand .dot{display:inline-block;background:var(--red)}
.brand.light{color:#fff}
.brand.light .dot{background:#fff}
.tiny{font-size:3.2px;line-height:1.5;color:var(--grey)}
.rule{height:1px;background:var(--line)}

/* folder */
.folder-cover{left:12px;top:12px;width:108px;height:306px;background:radial-gradient(circle at 50% 40%,#e0262c,var(--red-dark))}
.folder-cover .brand{position:absolute;left:14px;top:108px;font-size:26px}
.folder-cover .brand .dot{width:8px;height:8px}
.folder-cover .tagline{position:absolute;left:14px;top:140px;font-size:4px;color:#fff;letter-spacing:.3px}
.folder-cover .foot{position:absolute;left:14px;bottom:10px;font-size:3.2px;color:#f4c9ca}
.folder-inside{left:120px;top:12px;width:108px;height:306px}
.folder-inside .brand{position:absolute;left:10px;top:112px;font-size:11px}
.folder-inside .brand .dot{width:4px;height:4px}
.folder-inside .sub{position:absolute;left:10px;top:126px;font-size:3.4px;color:var(--grey)}
.folder-pockets{position:absolute;left:12px;top:262px}

/* sheets */
.sheet{top:96px;width:156px;height:240px;padding:10px 10px 0}
.sheet .brand{font-size:9px}
.sheet .brand .dot{width:4px;height:4px}
.sheet .bar{position:absolute;left:0;right:0;bottom:0;height:5px;background:var(--red)}
.doc-title{font-family:"Montserrat",Arial,sans-serif;font-weight:600;font-size:6px;color:var(--red);position:absolute;right:10px;top:12px}
.invoice{left:233px}
.fax{left:396px}
.letterhead{left:560px}
.grid{position:absolute;left:10px;right:10px}
.grid .row{height:5px;border-bottom:.5px solid var(--line)}
.grid .head{height:6px;background:var(--ink)}
.watermark{position:absolute;left:0;right:0;top:108px;text-align:center;font-family:"Montserrat",Arial,sans-serif;font-weight:800;font-size:46px;color:var(--faint)}

/* cards */
.card{top:30px;width:76px;height:44px;padding:6px}
.card .brand{font-size:7px}
.card .brand .dot{width:3px;height:3px}
.card-front{left:580px}
.card-back{left:662px}
.card-red{left:744px;background:var(--red)}
.card-black{left:826px;background:var(--ink)}
.card .name{font-family:"Montserrat",Arial,sans-serif;font-weight:600;font-size:4.4px;color:var(--ink)}
.card .role{font-size:3.2px;color:var(--red);margin-bottom:3px}
.card-black .name{color:#fff}
.card-black .tiny{color:#bbb}

/* envelopes */
.envelope{left:905px;width:284px}
.env-front{top:118px;height:104px;padding:10px}
.env-front .brand{font-size:10px}
.env-front .brand .dot{width:4px;height:4px}
.env-front .addr{position:absolute;left:130px;top:54px;width:110px}
.env-back-white{top:234px;height:52px;overflow:hidden}
.env-back-black{top:296px;height:52px;background:var(--ink);overflow:hidden}
.envelope svg{position:absolute;left:0;top:0}
</style>
</head>
<body>

<!-- presentation folder -->
<div class="piece folder-cover">
  <div class="brand light"><span class="dot"></span>TMK</div>
  <div class="tagline">BUILDING WORKS</div>
  <div class="foot">Certified Specialty Contractor</div>
</div>
<div class="piece folder-inside">
  <div class="brand"><span class="dot"></span>TMK</div>
  <div class="sub">BUILDING WORKS</div>
</div>
<svg class="folder-pockets" width="216" height="78" viewBox="0 0 216 78" aria-hidden="true">
  <path d="M0 8 L80 0 L108 14 L108 78 L0 78 Z" fill="#fff" stroke="#ddd" stroke-width=".5"/>
  <path d="M108 14 L136 0 L216 8 L216 78 L108 78 Z" fill="#fff" stroke="#ddd" stroke-width=".5"/>
  <rect x="150" y="30" width="40" height="22" fill="none" stroke="#e3e3e3" stroke-width=".5"/>
</svg>

<!-- invoice -->
<div class="piece sheet invoice">
  <div class="brand"><span class="dot"></span>TMK</div>
  <div class="doc-title">INVOICE</div>
  <div class="tiny" style="margin-top:4px">info@tmkbuildingworks.example<br>www.tmkbuildingworks.example</div>
  <div class="grid" style="top:46px">
    <div class="head"></div>
    <div class="row"></div><div class="row"></div><div class="row"></div>
  </div>
  <div class="grid" style="top:80px">
    <div class="head"></div>
    <div class="row"></div><div class="row"></div><div class="row"></div><div class="row"></div>
    <div class="row"></div><div class="row"></div><div class="row"></div><div class="row"></div>
    <div class="row"></div><div class="row"></div><div class="row"></div><div class="row"></div>
  </div>
  <div class="tiny" style="position:absolute;left:10px;bottom:12px">Thank you for your business. Payment due in thirty days.</div>
  <div class="bar"></div>
</div>

<!-- fax -->
<div class="piece sheet fax">
  <div class="brand"><span class="dot"></span>TMK</div>
  <div class="doc-title">FAX</div>
  <div class="grid" style="top:42px">
    <div class="row"></div><div class="row"></div><div class="row"></div><div class="row"></div>
  </div>
  <div class="tiny" style="position:absolute;left:10px;top:70px">Comments:</div>
  <div class="watermark">TMK</div>
  <div class="tiny" style="position:absolute;left:10px;bottom:12px">Framing · Drywall · Wall Textures · Acoustical Ceilings</div>
  <div class="bar"></div>
</div>

<!-- letterhead -->
<div class="piece sheet letterhead">
  <div class="brand"><span class="dot"></span>TMK</div>
  <div class="tiny" style="margin-top:3px">Certified Specialty Contractor · SCC284730592</div>
  <div class="rule" style="margin-top:6px"></div>
  <div class="watermark">TMK</div>
  <div class="tiny" style="position:absolute;left:10px;bottom:12px">info@tmkbuildingworks.example · www.tmkbuildingworks.example</div>
  <div class="bar"></div>
</div>

<!-- business cards -->
<div class="piece card card-front">
  <div class="brand" style="margin-top:10px"><span class="dot"></span>TMK</div>
  <div class="tiny">BUILDING WORKS</div>
</div>
<div class="piece card card-back">
  <div class="name">Radoslav Benek</div>
  <div class="role">Owner</div>
  <div class="tiny">info@tmkbuildingworks.example<br>www.tmkbuildingworks.example<br>SCC284730592</div>
</div>
<div class="piece card card-red">
  <div class="brand light" style="margin-top:10px"><span class="dot"></span>TMK</div>
  <div class="tiny" style="color:#f4c9ca">Certified Specialty Contractor</div>
</div>
<div class="piece card card-black">
  <div class="name">Radoslav Benek</div>
  <div class="role">Owner</div>
  <div class="tiny">Drywall Installation &amp; Finishing<br>Commercial &amp; Residential</div>
</div>

<!-- envelopes -->
<div class="piece envelope env-front">
  <div class="brand"><span class="dot"></span>TMK</div>
  <div class="tiny" style="margin-top:3px">www.tmkbuildingworks.example</div>
  <div class="addr tiny">Recipient Name<br>Street Address Line<br>City, State Zip</div>
</div>
<div class="piece envelope env-back-white">
  <svg width="284" height="52" viewBox="0 0 284 52" aria-hidden="true">
    <path d="M0 0 H284 V10 Q142 58 0 10 Z" fill="#f2f2f2"/>
    <path d="M0 0 H284 V6 Q142 44 0 6 Z" fill="var(--red)"/>
  </svg>
</div>
<div class="piece envelope env-back-black">
  <svg width="284" height="52" viewBox="0 0 284 52" aria-hidden="true">
    <path d="M0 0 H284 V8 Q142 56 0 8 Z" fill="var(--red)"/>
    <path d="M0 0 H284 V4 Q142 40 0 4 Z" fill="#fff"/>
  </svg>
</div>

</body>
</html>
```